Business Cards

Need a neat design for a new business card

Industry/Entity Type

Residential Construction

Contact Information for Business Card

Company Name- KOVE Construction Inc.
Owner- Marcus Tolliver
Phone number- (555)203-7481
Email- kovecohomes@brindlemail.example
Facebook- www.socialpage.example/kovecohomes

Colors
fefdec

```html
<!DOCTYPE html>
<html lang="en">
<head>
<meta charset="utf-8">
<title>KOVE Construction – Business Cards</title>
<link rel="stylesheet" href="https://fonts.googleapis.com/css2?family=Poppins:wght@400;500;600&display=swap">
<style>
  :root {
    --stage: #2b2c2f;
    --card-dark: #222528;
    --card-cream: #fefdec;
    --ink: #141414;
    --ink-soft: #2e2e2e;
    --on-dark: #f4f4ee;
  }
  * { box-sizing: border-box; margin: 0; padding: 0; }
  html, body {
    width: 1200px; height: 800px; overflow: hidden;
    background: var(--stage);
    font-family: "Poppins", Arial, sans-serif;
  }
  .stage {
    position: relative; width: 1200px; height: 800px;
  }
  .card {
    position: absolute; left: 320px; width: 560px; height: 320px;
    border-radius: 18px; overflow: hidden;
  }
  .card--back { top: 60px; background: var(--card-dark); }
  .card--front { top: 420px; background: var(--card-cream); color: var(--ink); }

  .brand {
    position: absolute; display: flex; align-items: center; gap: 10px;
    font-weight: 500; white-space: nowrap;
  }
  .brand__mark { width: 12px; height: 12px; flex: none; }
  .card--back .brand {
    left: 50%; top: 50%; transform: translate(-50%, -50%);
    color: var(--on-dark); font-size: 30px; letter-spacing: 1px;
  }
  .card--back .brand__mark { background: var(--on-dark); width: 16px; height: 16px; }
  .card--front .brand {
    left: 30px; top: 137px; font-size: 17px; color: var(--ink); letter-spacing: .3px;
  }
  .card--front .brand__mark { background: var(--ink); width: 11px; height: 11px; }

  .divider {
    position: absolute; left: 240px; top: 95px; width: 1px; height: 120px;
    background: var(--ink-soft);
  }

  .contact-person {
    position: absolute; left: 264px; top: 62px;
  }
  .contact-person__name { font-size: 18px; font-weight: 600; letter-spacing: .3px; text-transform: uppercase; }
  .contact-person__role { font-size: 11px; font-weight: 400; margin-top: -2px; }

  .contact-list {
    position: absolute; left: 264px; top: 128px; list-style: none;
    font-size: 11.5px; line-height: 24px;
  }
  .contact-list li { display: flex; align-items: center; gap: 8px; white-space: nowrap; }
  .contact-list svg { width: 11px; height: 11px; flex: none; }

  .footer-band {
    position: absolute; left: 0; right: 0; top: 254px; height: 38px;
    background: var(--ink); color: var(--on-dark);
    display: flex; align-items: center; justify-content: center;
    font-size: 12px; letter-spacing: 5px; white-space: nowrap;
  }
</style>
</head>
<body>
<main class="stage">
  <section class="card card--back" aria-label="Business card back">
    <div class="brand"><span class="brand__mark"></span>KOVE Construction</div>
  </section>

  <section class="card card--front" aria-label="Business card front">
    <div class="brand"><span class="brand__mark"></span>KOVE Construction</div>
    <div class="divider"></div>

    <div class="contact-person">
      <p class="contact-person__name">Marcus Tolliver</p>
      <p class="contact-person__role">CEO</p>
    </div>

    <ul class="contact-list">
      <li>
        <svg viewBox="0 0 12 12" aria-hidden="true"><rect x="1.5" y="1.5" width="9" height="9" rx="1" fill="none" stroke="currentColor" stroke-width="1.6"/></svg>
        (555)203-7481
      </li>
      <li>
        <svg viewBox="0 0 12 12" aria-hidden="true"><rect x="0.5" y="2" width="11" height="8" fill="currentColor"/><path d="M0.5 2 L6 7 L11.5 2" fill="none" stroke="#fefdec" stroke-width="1.2"/></svg>
        kovecohomes@brindlemail.example
      </li>
      <li>
        <svg viewBox="0 0 12 12" aria-hidden="true"><circle cx="6" cy="6" r="4.5" fill="currentColor"/></svg>
        www.socialpage.example/kovecohomes
      </li>
    </ul>

    <div class="footer-band">KOVE Construction Inc.</div>
  </section>
</main>
</body>
</html>
```